Marlow Vale community splash page

We need an elegant splash page with minimal information for a lake development project that will open next summer. You can see what we currently use at www.marlow-vale.com. Most of the existing information needs to be on the splash page.

Target Market(s)

People who are interested in purchasing lots at our lake community. Up scale housing on a private lake with marinas.

Industry/Entity Type

Community

Coding

Coded - Design and coding required

Requirements
Must have
• Must have contact information for Marlow Development LLC. Must have link to marketing plat file.
Nice to have
• Would be nice to have linking capability to prezi tour file already created. See tour here: http://tourvistaly.com/kq4mzpxw8rtn/?utm_campaign=share&utm_medium=copy&rc=ex0share
Should not have
• We want this standout, not be conservative or traditional. Must be elegant and bold.

```html
<!DOCTYPE html>
<html lang="en">
<head>
<meta charset="utf-8">
<title>Marlow Vale</title>
<link rel="stylesheet" href="https://fonts.googleapis.com/css2?family=Varela+Round&family=Open+Sans:wght@400;600&display=swap">
<style>
:root{
  --navy:#12357a;
  --brand:#1d4f9a;
  --sky-top:#8fbce6;
  --sky-mid:#bcd9ef;
  --forest:#6f8a36;
  --water:#3c4a2e;
  --panel:#0f4a8c;
  --btn-green:#1f8a3c;
  --ink:#4a4a4a;
  --muted:#7a7a7a;
  --line:#e2e2e2;
  --footer:#f4f4f4;
}
*{box-sizing:border-box;margin:0;padding:0}
html,body{width:1200px;height:1173px;overflow:hidden;background:#fff}
body{position:relative;font-family:"Open Sans",sans-serif;color:var(--ink)}
.site-header{position:absolute;top:0;left:0;width:1200px;height:96px}
.brand{position:absolute;left:163px;top:30px;display:flex;align-items:center;gap:10px;font-family:"Varela Round",sans-serif;font-size:30px;letter-spacing:3px;color:var(--brand);text-decoration:none}
.brand-mark{width:22px;height:22px;border-radius:50%;background:var(--brand)}
.header-nav{position:absolute;right:169px;top:33px;display:flex;align-items:center;gap:15px}
.header-nav a{font-family:"Varela Round",sans-serif;font-size:15px;text-decoration:none;color:var(--navy)}
.header-nav .sign-in{background:linear-gradient(#4a90d4,#2a6cb4);color:#fff;padding:0 15px;height:34px;line-height:34px;border-radius:2px}
.hero{position:absolute;top:96px;left:0;width:1200px;height:531px;
  background:linear-gradient(180deg,var(--sky-top) 0%,var(--sky-mid) 45%,#a5b55c 58%,var(--forest) 72%,#4d5a2a 82%,var(--water) 100%)}
.hero-arrow{position:absolute;top:205px}
.hero-copy{position:absolute;left:170px;top:155px;width:540px}
.hero-copy h1{font-family:"Varela Round",sans-serif;font-weight:400;font-size:42px;color:var(--navy);line-height:1.1}
.hero-copy h2{font-family:"Varela Round",sans-serif;font-weight:400;font-size:22px;color:#fff;margin-top:6px}
.hero-copy p{font-size:11px;line-height:19px;color:var(--navy);margin-top:8px;width:430px}
.btn-flyer{display:inline-block;margin-top:9px;width:216px;height:43px;line-height:43px;text-align:center;background:linear-gradient(#24a14a,var(--btn-green));color:#fff;font-family:"Varela Round",sans-serif;font-size:15px;text-decoration:none;border-radius:2px}
.signup{position:absolute;left:749px;top:119px;width:286px;height:316px;background:linear-gradient(#1a5aa0,var(--panel));padding:22px 24px 0 26px}
.signup h3{font-family:"Varela Round",sans-serif;font-weight:400;font-size:25px;color:#fff}
.signup form{margin-top:10px;display:flex;flex-direction:column;gap:6px}
.field{height:29px;border:1px solid #c9d6e6;background:#fff;font-family:"Open Sans",sans-serif;font-size:11px;color:#777;padding:0 11px;width:100%}
.field-row{display:flex;gap:6px}
.field-row .field{width:50%}
.btn-signup{margin-top:2px;height:40px;border:0;background:linear-gradient(#4b95da,#2567ad);color:#fff;font-family:"Varela Round",sans-serif;font-size:19px}
.intro{position:absolute;left:177px;top:693px;width:470px}
.intro h2{font-family:"Varela Round",sans-serif;font-weight:400;font-size:27px;color:#555;margin-left:3px}
.intro h3{font-family:"Varela Round",sans-serif;font-weight:400;font-size:17px;color:#555;margin:6px 0 0 3px}
.intro p{font-size:11px;line-height:18.5px;color:#555;margin-top:9px}
.btn-learn{display:inline-block;margin-top:14px;width:120px;height:32px;line-height:32px;text-align:center;background:linear-gradient(#1a4a90,#0f2f68);color:#fff;font-family:"Varela Round",sans-serif;font-size:13.5px;text-decoration:none}
.tour{position:absolute;left:691px;top:688px;width:344px;height:213px;border:1px solid #d6d6d6;background:#fff;padding:7px;box-shadow:0 0 3px rgba(0,0,0,.1)}
.tour-poster{width:100%;height:100%;background:linear-gradient(#ececee,#e6e6ea);position:relative;display:block}
.tour-play{position:absolute;left:159px;top:81px}
.divider{position:absolute;left:167px;top:987px;width:866px;border-top:1px solid var(--line)}
.partners{position:absolute;left:225px;top:1020px;width:770px;display:flex;justify-content:space-between;align-items:center}
.partner{display:flex;align-items:center;gap:5px;font-size:10px;color:#666;font-weight:600}
.partner i{display:block;width:14px;height:14px;background:#777}
.site-footer{position:absolute;top:1104px;left:0;width:1200px;height:69px;background:var(--footer);border-top:1px solid #e6e6e6}
.site-footer p{position:absolute;left:167px;top:24px;font-size:11.5px;color:var(--muted)}
.site-footer p a{color:var(--muted);text-decoration:none}
.social{position:absolute;right:181px;top:19px;display:flex;gap:8px}
.social a{display:block;width:22px;height:22px;border-radius:3px}
</style>
</head>
<body>
<header class="site-header">
  <a class="brand" href="#"><span class="brand-mark"></span>MARLOW VALE</a>
  <nav class="header-nav">
    <a href="#">Create Account</a>
    <a class="sign-in" href="#">Sign In</a>
  </nav>
</header>

<section class="hero" role="img" aria-label="Photo of a calm lake lined with autumn trees under a blue sky">
  <svg class="hero-arrow" style="left:86px" width="36" height="80" viewBox="0 0 36 80"><polyline points="33,2 3,40 33,78" fill="none" stroke="#fff" stroke-width="2"/></svg>
  <svg class="hero-arrow" style="left:1066px" width="36" height="80" viewBox="0 0 36 80"><polyline points="3,2 33,40 3,78" fill="none" stroke="#fff" stroke-width="2"/></svg>
  <div class="hero-copy">
    <h1>Mauris lacus vestibulum</h1>
    <h2>Suspendisse quam leo molestie sed luctus</h2>
    <p>libero a tempus libero lectus feugiat felis Morbi diam mauris viverra in gravida eu mattis in ante Morbi eget arcu Morbi porta libero id ullamcorper</p>
    <a class="btn-flyer" href="#">Download Marketing flyer</a>
  </div>
  <aside class="signup">
    <h3>Sign Up Member</h3>
    <form>
      <input class="field" placeholder="Your Name">
      <input class="field" placeholder="Email address">
      <input class="field" placeholder="Phone">
      <div class="field-row"><input class="field" placeholder="City"><input class="field" placeholder="State"></div>
      <input class="field" placeholder="Query/Tittle">
      <button class="btn-signup" type="button">Sign Up Now</button>
    </form>
  </aside>
</section>

<section class="intro">
  <h2>Morbi ornare gravida Integer congue</h2>
  <h3>Praesent elementum elit at tellus nec ultricies sit</h3>
  <p>Vivamus porttitor g purus nisi eleifend libero a tempus libero lectus feugiat felis Morbi diam mauris viverra in gravida eu mattis in ante Morbi eget arcu Morbi porta libero id ullamcorper nonummy nibh ligula pulvinar metus eget consectetuer augu</p>
  <p>Morbi ornare gravida elit Integer congue augue et malesuada iaculis ipsum dui aliquet felis at cursus magna nisl nec elit Praesent elementum elit at tellus nec</p>
  <a class="btn-learn" href="#">Learn More</a>
</section>

<figure class="tour">
  <a class="tour-poster" href="http://tourvistaly.com/kq4mzpxw8rtn/?utm_campaign=share&utm_medium=copy&rc=ex0share" role="img" aria-label="Tour video poster with hand-lettered Marlow Vale title and tagline">
    <svg class="tour-play" width="30" height="30" viewBox="0 0 30 30"><circle cx="15" cy="15" r="15" fill="#fff"/><polygon points="12,9 21,15 12,21" fill="#111"/></svg>
  </a>
</figure>

<div class="divider"></div>
<section class="partners" aria-label="Partners">
  <span class="partner"><i></i>Norland Trust</span>
  <span class="partner"><i></i>Horizon Aid</span>
  <span class="partner"><i></i>Keelpoint</span>
  <span class="partner"><i></i>Vellmar Reserve</span>
  <span class="partner"><i></i>Clearview Fund</span>
  <span class="partner"><i></i>Brenko</span>
  <span class="partner"><i></i>Greenrow Institute</span>
  <span class="partner"><i></i>Solace Health</span>
</section>

<footer class="site-footer">
  <p>© 2014 Marlow Development LLC&nbsp; <a href="http://www.marlow-vale.com">www.marlow-vale.com</a>&nbsp; All right reserved&nbsp; Term of Use</p>
  <div class="social">
    <a href="#" style="background:#c4302b" aria-label="Video channel"></a>
    <a href="#" style="background:#3b5998" aria-label="Social page"></a>
    <a href="#" style="background:#4ab3e8" aria-label="Social feed"></a>
    <a href="#" style="background:#cb2027" aria-label="Image board"></a>
  </div>
</footer>
</body>
</html>
```